Marla's Hair and Wigs: Back to School Sale

I need a "Back to School" sale flyer: I sell hair extensions and fashion wigs to a very diverse clientele. The sale will include:
20% OFF: Synthetic Hair Extensions
20% OFF: Synthetic Hair Pieces
15% OFF: Human Hair Extensions
25% OFF: Jewelry/Accessories
Starts: Thursday, August 3rd to Saturday, August 5th

Target Market(s)

women of all ethnic backgrounds and between the ages of 16-60

Industry/Entity Type

Hair And Beauty

Font styles to use
Sans Serif

Colors
e34197

Requirements
Must have
• High resolution for printing posters and flyers. As well as posting on social media: Instagram/Facebook
• Eye catching graphics

```html
<!DOCTYPE html>
<html lang="en">
<head>
<meta charset="utf-8">
<title>Marla's Hair and Wigs – Back to School Sale</title>
<link rel="stylesheet" href="https://fonts.googleapis.com/css2?family=Josefin+Sans:wght@300;400;600&family=Kaushan+Script&display=swap">
<style>
  :root {
    --magenta: #e34197;
    --magenta-deep: #c8197f;
    --pink-soft: #f4a9cf;
    --ink: #1c1c1c;
    --paper: #ffffff;
    --backdrop: #f3f1ec;
    --hair-dark: #4a3a33;
    --hair-mid: #7a5a48;
  }
  * { margin: 0; padding: 0; box-sizing: border-box; }
  html, body {
    width: 1200px; height: 900px; overflow: hidden;
    background: var(--backdrop);
  }
  .flyer {
    position: absolute;
    left: 320px; top: 40px;
    width: 560px; height: 820px;
    overflow: hidden;
    background: linear-gradient(180deg, var(--paper) 0%, var(--paper) 22%, #f7cfe3 45%, var(--pink-soft) 65%, var(--magenta) 100%);
    box-shadow: 0 12px 30px rgba(0,0,0,0.12);
    font-family: "Josefin Sans", sans-serif;
  }
  .brand {
    position: absolute; top: 70px; left: 0; width: 100%;
    display: flex; align-items: center; justify-content: center; gap: 12px;
  }
  .brand-mark {
    width: 22px; height: 22px; background: var(--magenta);
  }
  .brand-name {
    font-family: "Josefin Sans", sans-serif;
    font-weight: 400; font-size: 28px; letter-spacing: 1px;
    color: var(--ink);
  }
  .headline {
    position: absolute; top: 150px; left: 0; width: 100%;
    text-align: center;
    transform: rotate(-9deg);
  }
  .title {
    font-family: "Kaushan Script", cursive;
    font-size: 72px; color: var(--ink); line-height: 1;
  }
  .date-banner {
    display: inline-block; margin-top: 14px;
    background: var(--magenta); color: var(--paper);
    font-weight: 600; font-size: 19px;
    padding: 8px 34px;
    clip-path: polygon(0 0, 100% 0, 96% 50%, 100% 100%, 0 100%, 4% 50%);
  }
  .date-banner sup { font-size: 11px; }
  .offers { position: absolute; inset: 0; }
  .offer {
    position: absolute; width: 128px; height: 128px; border-radius: 50%;
    overflow: hidden; background: var(--paper);
    box-shadow: 0 4px 10px rgba(0,0,0,0.18);
    text-align: center;
  }
  .offer-rate {
    height: 56px; background: var(--magenta); color: var(--paper);
    display: flex; align-items: flex-end; justify-content: center;
    padding-bottom: 4px;
    font-weight: 300; font-size: 34px;
  }
  .offer-rate small { font-size: 14px; margin-left: 3px; margin-bottom: 6px; }
  .offer-label {
    padding-top: 12px; font-weight: 400; font-size: 14px; line-height: 1.3; color: var(--ink);
  }
  .offer-1 { left: 40px; top: 400px; }
  .offer-2 { left: 168px; top: 375px; }
  .offer-3 { left: 296px; top: 350px; }
  .offer-4 { left: 424px; top: 325px; }
  .photo {
    position: absolute; left: 110px; top: 555px; width: 360px; height: 265px;
    border-radius: 120px 120px 0 0;
    background: linear-gradient(90deg, var(--hair-dark), var(--hair-mid) 50%, var(--hair-dark));
    opacity: 0.85;
  }
</style>
</head>
<body>
  <main class="flyer">
    <header class="brand">
      <span class="brand-mark"></span>
      <span class="brand-name">Marla's Hair and Wigs</span>
    </header>

    <section class="headline">
      <h1 class="title">Back to School!</h1>
      <p class="date-banner">Starts : Thursday, August 3<sup>rd</sup> to Saturday, August 5<sup>th</sup></p>
    </section>

    <section class="offers">
      <div class="offer offer-1">
        <div class="offer-rate">20%<small>OFF</small></div>
        <div class="offer-label">Synthetic<br>Hair Extensions</div>
      </div>
      <div class="offer offer-2">
        <div class="offer-rate">20%<small>OFF</small></div>
        <div class="offer-label">Synthetic<br>Hair Pieces</div>
      </div>
      <div class="offer offer-3">
        <div class="offer-rate">15%<small>OFF</small></div>
        <div class="offer-label">Human<br>Hair Extensions</div>
      </div>
      <div class="offer offer-4">
        <div class="offer-rate">25%<small>OFF</small></div>
        <div class="offer-label">Jewelry/<br>Accessories</div>
      </div>
    </section>

    <div class="photo" role="img" aria-label="Photo of three young women seen from behind with long flowing hair"></div>
  </main>
</body>
</html>
```